Spa Business Card Design Project

Hello! We are a boutique spa for men and women that is rebranding. I would like a memorable new business card that showcases our beautiful new logo and our unique business. I would like it to be classic/timeless and eclectic/artistic at the  same time.
I am a fan of negative space as you can tell from the logo. I am also open to any creative ideas.
Multi sided design. Two sided design is acceptable as an option, too. "Flaps/folds/whatever the design term is" are optional- whether full vertical or horizontal, half flap, full flap etc
On either side next to the golden snail I would potentially like to see "slow down. Enjoy Life."  Possibly on one statment on top of each other, crowned with the snail. Or the statment following the snail on one line... I am open for a creative suprise, too.
The back I would like room for the standard Information
"3817 Birch Lane
Elmbrook, Vermont 05762
(518) 462 3085
info@thecorvella spa.com
The snail is to be done in gold ink.
Can I also Have an option for cards that are individualized for staff members, too?

Updates
Project Deadline Extended
Reason: I apologize for the deadline extension. My day was more involved than anticipated in other matters. Hope to have this closed by next Tuesday.
Thank you

Target Market(s)
Men and women with expendable income between the ages of 30-55
Industry/Entity Type
Boutique
Requirements
Must have
- only black and gold ink.

Nice to have
- One of a kind.
Showcase the snail :-)
make you smile :-)
Fun, but professional.
Should not have
- Lots of color.
Too feminine.
Too busy.

```html
<!DOCTYPE html>
<html lang="en">
<head>
<meta charset="utf-8">
<title>The Corvella Spa – Business Cards</title>
<link rel="stylesheet" href="https://fonts.googleapis.com/css2?family=Jost:wght@400&display=swap">
<style>
  :root {
    --ink: #111111;
    --gold: #d2a862;
    --card: #ffffff;
    --card-edge: #7a7a7a;
    --stage-center: #ffffff;
    --stage-edge: #f8f3e6;
  }
  * { margin: 0; padding: 0; box-sizing: border-box; }
  html, body { width: 1200px; height: 900px; overflow: hidden; }
  body {
    position: relative;
    background: radial-gradient(ellipse at center, var(--stage-center) 55%, var(--stage-edge) 100%);
    font-family: "Jost", sans-serif;
    font-weight: 400;
    color: var(--ink);
  }
  .card {
    position: absolute;
    width: 454px;
    height: 260px;
    background: var(--card);
    border: 1px solid var(--card-edge);
  }
  .card--front { left: 373px; top: 124px; }
  .card--back-general { left: 111px; top: 465px; }
  .card--back-staff { left: 634px; top: 465px; }

  .brand {
    position: absolute;
    left: 0; right: 0;
    text-align: center;
    font-weight: 400;
  }
  .brand__name {
    top: 88px;
    font-size: 44px;
    line-height: 48px;
    letter-spacing: 1px;
  }
  .brand__tagline {
    top: 182px;
    font-size: 16px;
    line-height: 20px;
  }

  .emblem {
    position: absolute;
    left: 79px;
    top: 76px;
    width: 48px;
    height: 48px;
    border-radius: 50%;
    background: var(--gold);
  }
  .motto {
    position: absolute;
    left: 42px;
    width: 120px;
    top: 147px;
    text-align: center;
    font-size: 17px;
    line-height: 22px;
  }
  .divider {
    position: absolute;
    left: 192px;
    top: 58px;
    width: 1.5px;
    height: 135px;
    background: var(--gold);
  }
  .contact {
    position: absolute;
    left: 226px;
    font-size: 16px;
    line-height: 19px;
    font-style: normal;
  }
  .card--back-general .contact { top: 85px; }
  .card--back-staff .contact { top: 102px; }
  .contact__line--gap { margin-top: 6px; }
  .staff-name {
    position: absolute;
    left: 226px;
    top: 48px;
    font-size: 20px;
    line-height: 24px;
  }
</style>
</head>
<body>
  <section class="card card--front" aria-label="Card front">
    <h1 class="brand brand__name">The Corvella Spa</h1>
    <p class="brand brand__tagline">a quiet retreat for Men &amp; Women</p>
  </section>

  <section class="card card--back-general" aria-label="Card back, general">
    <span class="emblem" aria-hidden="true"></span>
    <p class="motto">Pause Here<br>Feel Well</p>
    <span class="divider" aria-hidden="true"></span>
    <address class="contact">
      <div>3817 Birch Lane</div>
      <div>Elmbrook, Vermont 05762</div>
      <div class="contact__line--gap">518 · 462 · 3085</div>
      <div class="contact__line--gap">info@thecorvellaspa.com</div>
    </address>
  </section>

  <section class="card card--back-staff" aria-label="Card back, staff">
    <span class="emblem" aria-hidden="true"></span>
    <p class="motto">Pause Here<br>Feel Well</p>
    <span class="divider" aria-hidden="true"></span>
    <p class="staff-name">Jane Smith</p>
    <address class="contact">
      <div>3817 Birch Lane</div>
      <div>Elmbrook, Vermont 05762</div>
      <div class="contact__line--gap">518 · 462 · 3085</div>
      <div class="contact__line--gap">info@thecorvellaspa.com</div>
    </address>
  </section>
</body>
</html>
```